Support People to improve their image and well-being by provided personalised advise

We need a design for business cards that could be used for production on brightleaf press. We build a new business in our region for advising mostly women (also men though) on style embracing several aspects including fashion, style, self-confidence and ultimately your internal and external image. The business card should be "classy", "french-style". The business is located in the french -speaking part of Switzerland, close to France. The name of the company is Lunor Mode

Target Market(s)

Service fees won't be cheap (medium to premium) thus we target mid-class to upper-class women (1st target) and men (2nd target)

Industry/Entity Type

Life Coaching

Contact Information for Business Card

Conseil en Image

+41 78 514 62 07
selmaroux@lunor-mode.example
linkedin.com/in/roux-dal-selma

Logo Text

Lunor Mode

Colors

Designer to choose colors to be used in the design.

```html
<!DOCTYPE html>
<html lang="fr">
<head>
<meta charset="utf-8">
<title>Lunor Mode — Cartes de visite</title>
<link rel="stylesheet" href="https://fonts.googleapis.com/css2?family=Questrial&family=Oswald:wght@500&display=swap">
<style>
  :root {
    --page-bg: #e7e5e2;
    --card-white: #ffffff;
    --pattern-light: #f4f3f3;
    --pattern-mid: #e9e7e8;
    --ink: #1b1b1b;
    --ink-soft: #444444;
    --rule: #2a2a2a;
    --back-dark: #0d0d0d;
    --back-mid: #1e1e1e;
    --back-mark: #262626;
  }
  * { box-sizing: border-box; margin: 0; padding: 0; }
  html, body { width: 1200px; height: 900px; overflow: hidden; }
  body {
    background: var(--page-bg);
    display: flex;
    flex-direction: column;
    align-items: center;
    justify-content: center;
    gap: 40px;
    font-family: "Questrial", "Helvetica Neue", sans-serif;
  }
  .card {
    position: relative;
    width: 680px;
    height: 389px;
    box-shadow: 0 6px 18px rgba(0,0,0,0.18);
    overflow: hidden;
  }

  /* Back */
  .card--back {
    background: linear-gradient(120deg, var(--back-dark) 0%, var(--back-mid) 55%, var(--back-dark) 100%);
  }
  .back-mark {
    position: absolute;
    right: 70px;
    top: 120px;
    display: flex;
    align-items: center;
    gap: 16px;
    color: var(--back-mark);
    font-size: 58px;
    letter-spacing: 1px;
  }
  .back-mark .dot {
    width: 40px; height: 40px;
    border: 2px solid var(--back-mark);
    border-radius: 50%;
  }

  /* Front */
  .card--front { background: var(--card-white); }
  .floral-pattern {
    position: absolute; inset: 0;
    background: radial-gradient(ellipse at 40% 45%, var(--pattern-light) 0%, var(--pattern-mid) 100%);
  }
  .front-logo {
    position: absolute;
    left: 0; right: 0;
    top: 70px;
    display: flex;
    justify-content: center;
    align-items: center;
    gap: 10px;
    color: var(--ink);
    font-size: 22px;
    letter-spacing: 2px;
  }
  .front-logo .dot {
    width: 14px; height: 14px;
    border: 1.5px solid var(--ink);
    border-radius: 50%;
  }
  .brand {
    position: absolute;
    left: 0; right: 0;
    top: 192px;
  }
  .brand-name-row {
    display: flex;
    align-items: center;
    padding-left: 262px;
  }
  .brand-name {
    font-size: 34px;
    color: var(--ink);
    letter-spacing: 1px;
  }
  .brand-rule { height: 1px; background: var(--rule); }
  .brand-name-row .brand-rule { width: 120px; margin-left: 14px; margin-top: 6px; }
  .tagline-row {
    display: flex;
    align-items: center;
    padding-left: 145px;
    margin-top: 4px;
  }
  .tagline-row .brand-rule { width: 112px; margin-right: 10px; }
  .tagline {
    font-size: 13px;
    letter-spacing: 7px;
    color: var(--ink-soft);
  }
  .contact {
    position: absolute;
    left: 0; right: 0;
    top: 284px;
    display: flex;
    justify-content: center;
    align-items: center;
    gap: 10px;
    font-family: "Oswald", "Arial Narrow", sans-serif;
    font-weight: 500;
    font-size: 14px;
    color: var(--ink);
  }
  .contact .sep { width: 1px; height: 14px; background: var(--ink-soft); }
</style>
</head>
<body>
  <section class="card card--back" aria-label="Verso de la carte">
    <div class="back-mark"><span class="dot"></span><span>Lunor Mode</span></div>
  </section>

  <section class="card card--front" aria-label="Recto de la carte">
    <div class="floral-pattern" role="img" aria-label="Motif floral baroque gris très pâle en fond"></div>
    <div class="front-logo"><span class="dot"></span><span>Lunor Mode</span></div>
    <div class="brand">
      <div class="brand-name-row">
        <h1 class="brand-name">Lunor Mode</h1>
        <span class="brand-rule"></span>
      </div>
      <div class="tagline-row">
        <span class="brand-rule"></span>
        <p class="tagline">Conseil en Image</p>
      </div>
    </div>
    <p class="contact">
      <span>+41 78 514 62 07</span><span class="sep"></span>
      <span>selmaroux@lunor-mode.example</span><span class="sep"></span>
      <span>linkedin.com/in/roux-dal-selma</span>
    </p>
  </section>
</body>
</html>
```